ReDesign Website for a more Bold approach

Hello! I'd like to redesign my website: holvencrest.com

I'd like to add one thing that's not on my website which is a blog. The design around the blog should be put time into as I will be putting out incredibly great content and want it to attract viewers.

I get a lot of inspiration from ruvtal.com (the way they flow the big statements across each screen, colors)
moorlane.vc (the simplicity behind the design is beautiful)

I like modern very simple but bold approaches.

I am going to attach my logo here and if it can be thought of when making the design of the website. Thanks!

Industry/Entity Type

Finance and Private Equity

Number of Pages Required

3 page

Font styles to use
Serif
Sans Serif

Colors
0054AA
0677BA
7BADD7
CADEEF
E8F1F8
0094D4
00A9DD
6FCCEA
C7EBF8
E9F6FB
00AB8E
00BBA5
67D7C9
C6EFE9
E9F9F6

Requirements
Must have
• My project must have a Home, Expertise, Story, Clients, Approach, Blog, Contact
Nice to have
• It would be nice to have these tabs reduced to 1-3 pages
Should not have
• My project must not have bright colors.

```html
<!DOCTYPE html>
<html lang="en">
<head>
<meta charset="utf-8">
<title>Holvencrest Ventures</title>
<link rel="stylesheet" href="https://fonts.googleapis.com/css2?family=Open+Sans:wdth,wght@75..100,400..800&family=Poppins:wght@400;500;600&display=swap">
<style>
:root{
  --navy:#0b3a6e;
  --navy-deep:#082b52;
  --blue:#0054AA;
  --accent:#00AB8E;
  --accent-soft:#C6EFE9;
  --sky:#7BADD7;
  --mist:#E8F1F8;
  --white:#ffffff;
  --ink:#1d2533;
  --muted:#555c66;
  --frame:#ebecee;
  --field:#CADEEF;
  --foot-text:#CADEEF;
}
*{box-sizing:border-box;margin:0;padding:0}
html,body{width:1200px;height:4830px;overflow:hidden}
body{background:var(--frame);font-family:"Poppins",sans-serif;color:var(--ink);position:relative}
.backdrop-top{position:absolute;left:0;top:0;width:1200px;height:640px;background:var(--navy)}
.page{position:absolute;left:37px;top:0;width:1126px;height:4781px;background:var(--white);box-shadow:0 10px 40px rgba(0,0,0,.18);overflow:hidden}
.abs{position:absolute}
.head{font-family:"Open Sans",sans-serif;font-stretch:75%;font-weight:800}

/* nav */
.nav{left:0;top:0;width:1126px;height:71px;background:var(--navy)}
.brand{font-family:"Open Sans",sans-serif;font-weight:700;font-size:19px;letter-spacing:.5px;color:var(--white)}
.nav .brand{left:188px;top:31px}
.nav-link{top:37px;font-size:11px;color:var(--white)}
.nav-cta{left:840px;top:30px;width:98px;height:32px;background:var(--accent);color:var(--white);font-size:11px;display:flex;align-items:center;justify-content:center}

/* hero */
.hero{left:0;top:71px;width:1126px;height:520px;background:linear-gradient(90deg,#e6e9ee 0%,#e1e5ea 38%,#d6dbe2 55%,#cfd3da 75%,#e6e8ec 100%)}
.hero-title{left:186px;top:160px;font-size:52px;line-height:56px;color:var(--navy);letter-spacing:.5px}
.hero-title .accent{color:var(--accent)}
.hero-text{left:188px;top:290px;width:380px;font-size:11px;line-height:18px;color:var(--ink)}
.btn{background:var(--accent);color:var(--white);font-size:11px;display:flex;align-items:center;justify-content:center}
.hero-btn{left:188px;top:379px;width:98px;height:26px}
.hero-dots{left:188px;top:497px;display:flex;gap:6px}
.hero-dots span{width:22px;height:5px;border-radius:3px;background:var(--navy)}
.hero-dots span.on{background:var(--accent)}
.dot-grid{display:grid;grid-template-columns:repeat(6,4px);gap:8px}
.dot-grid i{width:4px;height:4px;border-radius:50%;background:#b9c6d4}

/* stats */
.stat{top:669px;width:178px;height:175px;color:var(--white);text-align:center;box-shadow:0 10px 24px rgba(11,58,110,.2)}
.stat.navy{background:var(--navy)}
.stat.red{background:var(--accent)}
.stat svg{margin-top:30px}
.stat-num{font-family:"Open Sans",sans-serif;font-weight:700;font-size:27px;margin-top:14px}
.stat-label{font-size:12px;margin-top:6px}

/* story / approach */
.section-title{font-family:"Open Sans",sans-serif;font-weight:700;font-size:25px;color:var(--navy);letter-spacing:.3px}
.body-text{font-size:11.5px;line-height:17.6px;color:var(--ink)}
.body-text p+p{margin-top:16px}
.story-photo{left:188px;top:913px;width:386px;height:407px;background:linear-gradient(160deg,#d6dce4 0%,#9aa6b4 45%,#4b566a 70%,#c6ced8 100%)}

/* expertise */
.center-title{left:0;width:1126px;text-align:center;font-family:"Open Sans",sans-serif;font-weight:700;font-size:25px}
.on-dark{color:var(--white)}
.on-light{color:var(--navy)}
.exp-card{width:240px;height:264px;overflow:hidden}
.exp-photo{position:absolute;inset:0}
.exp-red{position:absolute;inset:0;background:var(--accent);clip-path:polygon(0 52%,50% 72%,100% 52%,100% 100%,0 100%)}
.exp-icon{position:absolute;left:95px;top:148px;width:50px;height:50px;border-radius:50%;background:var(--white);display:flex;align-items:center;justify-content:center}
.exp-label{position:absolute;left:0;right:0;top:223px;text-align:center;font-family:"Open Sans",sans-serif;font-weight:700;font-size:13px;color:var(--white)}

/* testimonials */
.t-card{top:2366px;width:240px;height:297px;background:var(--white);box-shadow:0 6px 26px rgba(0,0,0,.12);text-align:center}
.t-quote{position:absolute;left:20px;top:-6px;width:38px;height:32px;background:var(--accent);color:var(--white);font-family:"Open Sans",sans-serif;font-weight:800;font-size:20px;line-height:38px}
.t-avatar{width:58px;height:58px;border-radius:50%;background:linear-gradient(180deg,#e8eaee,#b9c0ca);margin:44px auto 0}
.t-name{font-family:"Open Sans",sans-serif;font-weight:700;font-size:16px;color:var(--navy);margin-top:22px}
.t-text{font-size:11px;line-height:17px;color:var(--muted);margin:14px 22px 0}
.t-stars{margin-top:14px;display:flex;justify-content:center;gap:4px}
.pager{display:flex;gap:14px;align-items:center;justify-content:center;left:0;width:1126px}
.pager i{width:10px;height:10px;border-radius:50%;background:var(--accent-soft)}
.pager i.on{width:16px;height:16px;border:2px solid var(--accent);background:var(--white);position:relative}
.pager i.on::after{content:"";position:absolute;left:3px;top:3px;width:6px;height:6px;border-radius:50%;background:var(--accent)}
.pager.dark i{background:#2c5585}

.approach-photo{left:552px;top:2826px;width:388px;height:420px;background:radial-gradient(ellipse at 50% 78%,#c9a43a 0%,#3a3a3a 30%,#b9b8b6 55%,#d6d2cd 100%)}

/* blog */
.b-card{top:3536px;width:244px;height:347px;background:var(--white)}
.b-photo{position:absolute;left:0;top:0;width:244px;height:184px}
.b-date{position:absolute;left:26px;top:148px;width:54px;height:60px;background:var(--accent);color:var(--white);font-family:"Open Sans",sans-serif;font-weight:700;font-size:14px;line-height:18px;text-align:center;padding-top:12px}
.b-title{position:absolute;left:26px;top:233px;font-family:"Open Sans",sans-serif;font-weight:700;font-size:13.5px;color:var(--ink)}
.b-text{position:absolute;left:26px;top:258px;width:200px;font-size:9px;line-height:15px;color:var(--muted)}
.b-more{position:absolute;left:26px;top:302px;font-size:9px;font-weight:600;color:var(--accent)}

/* contact */
.field{border:1.5px solid var(--field);border-radius:3px;font-size:10.5px;color:var(--ink);padding:9px 14px}
.submit{left:295px;top:4399px;width:536px;height:45px;background:var(--accent);border-radius:3px;color:var(--white);font-family:"Open Sans",sans-serif;font-weight:700;font-size:20px;display:flex;align-items:center;justify-content:center}

/* footer */
.footer{left:0;top:4509px;width:1126px;height:272px;background:var(--navy-deep);color:var(--white)}
.footer .brand{left:188px;top:78px;font-size:20px}
.foot-about{left:188px;top:120px;width:210px;font-size:8.5px;line-height:13.5px;color:var(--foot-text)}
.foot-head{font-family:"Open Sans",sans-serif;font-weight:700;font-size:11.5px}
.foot-list{list-style:none;font-size:8.5px;line-height:20.5px;color:var(--foot-text)}
.foot-list li{display:flex;align-items:center;gap:8px}
.foot-list .mk{width:8px;height:8px;border-radius:50%;background:var(--white);flex:none}
.foot-copy{left:0;top:242px;width:1126px;text-align:center;font-size:8.5px;color:var(--foot-text)}
.foot-rule{left:0;top:230px;width:1126px;height:1px;background:#17406d}
</style>
</head>
<body>
<div class="backdrop-top"></div>

<main class="page">

  <!-- hero -->
  <div class="abs hero" role="img" aria-label="Two businesswomen reviewing documents at a desk with a laptop"></div>
  <div class="abs dot-grid" style="left:160px;top:142px">
    <i></i><i></i><i></i><i></i><i></i><i></i><i></i><i></i><i></i><i></i><i></i><i></i><i></i><i></i><i></i><i></i><i></i><i></i><i></i><i></i><i></i><i></i><i></i><i></i>
  </div>
  <h1 class="abs head hero-title">BUILT BYFOUNDERS<br><span class="accent">FOR FOUNDERS</span></h1>
  <p class="abs hero-text">Lorem ipsum dolor sit amet, consectetur adipiscing elit, sed do eiusmod tempor incididunt ut labore et dolore magna aliqua. Quis ipsum suspendisse ultrices gravida. Risus commodo</p>
  <a class="abs btn hero-btn">Read More</a>
  <div class="abs hero-dots"><span></span><span class="on"></span><span></span></div>
  <svg class="abs" style="left:0;top:470px" width="1126" height="170" viewBox="0 0 1126 170">
    <polygon points="0,95 1126,25 1126,170 0,170" fill="#ffffff"/>
    <polygon points="880,82 1126,26 1126,128" fill="#00AB8E"/>
  </svg>

  <!-- nav -->
  <header class="abs nav">
    <div class="abs brand">HOLVENCREST VENTURES</div>
    <a class="abs nav-link" style="left:473px">Home</a>
    <a class="abs nav-link" style="left:537px">Expertise</a>
    <a class="abs nav-link" style="left:623px">Story</a>
    <a class="abs nav-link" style="left:690px">Client</a>
    <a class="abs nav-link" style="left:760px">Approach</a>
    <a class="abs nav-cta">Contact</a>
  </header>

  <!-- stats -->
  <div class="abs stat navy" style="left:188px">
    <svg width="40" height="36" viewBox="0 0 40 36" fill="none" stroke="#fff" stroke-width="1.6"><path d="M14 8h12l-3-6h-6z"/><path d="M12 10c-6 6-7 22 8 22s14-16 8-22z"/><text x="16" y="26" fill="#fff" stroke="none" font-size="11" font-family="Poppins">$</text></svg>
    <div class="stat-num">$40M+</div><div class="stat-label">Money Raised</div>
  </div>
  <div class="abs stat red" style="left:379px">
    <svg width="40" height="36" viewBox="0 0 40 36" fill="none" stroke="#fff" stroke-width="1.6"><circle cx="22" cy="10" r="7"/><path d="M4 26l8-5h10l4 3h-9"/><path d="M12 30h14l10-8"/></svg>
    <div class="stat-num">$40M+</div><div class="stat-label">Attributed Revenue</div>
  </div>
  <div class="abs stat navy" style="left:569px">
    <svg width="40" height="36" viewBox="0 0 40 36" fill="none" stroke="#fff" stroke-width="1.6"><rect x="12" y="4" width="16" height="28"/><rect x="4" y="14" width="8" height="18"/><rect x="28" y="12" width="8" height="20"/><path d="M16 10h3M21 10h3M16 16h3M21 16h3M16 22h3M21 22h3"/></svg>
    <div class="stat-num">11</div><div class="stat-label">Company Exits</div>
  </div>
  <div class="abs stat red" style="left:760px">
    <svg width="40" height="36" viewBox="0 0 40 36" fill="none" stroke="#fff" stroke-width="1.6"><circle cx="20" cy="13" r="10"/><circle cx="20" cy="13" r="5"/><path d="M13 21l-3 12 5-3 3 4 2-9M27 21l3 12-5-3-3 4-2-9"/></svg>
    <div class="stat-num">2</div><div class="stat-label">Award Won</div>
  </div>

  <!-- story -->
  <div class="abs dot-grid" style="left:160px;top:890px">
    <i></i><i></i><i></i><i></i><i></i><i></i><i></i><i></i><i></i><i></i><i></i><i></i><i></i><i></i><i></i><i></i><i></i><i></i><i></i><i></i><i></i><i></i><i></i><i></i>
  </div>
  <div class="abs story-photo" role="img" aria-label="Business team meeting around a table with a tablet in a bright office"></div>
  <h2 class="abs section-title" style="left:640px;top:915px">OUR STORY</h2>
  <div class="abs body-text" style="left:642px;top:964px;width:300px">
    <p>Holvencrest Ventures is a venture capital studio firm based in Austin TX with a laser focus on raising solid capital for startups and helping businesses jumpstart their revenue.</p>
    <p>Founded in 2020 by investment expert Daniel Ashcombe, Holvencrest Ventures combines proven experience in the venture capital field with a data-driven business analysis strategy to secure capital and reinforce revenue streams for startups and established businesses. Born from the idea that the best way to help founders thrive is to understand their strengths, their weaknesses, their ambitions and their needs - our specialists have been through the entire startup process themselves, and that experience forms our unique</p>
  </div>
  <a class="abs btn" style="left:642px;top:1281px;width:99px;height:26px">Read More</a>

  <!-- expertise -->
  <svg class="abs" style="left:0;top:1395px" width="1126" height="890" viewBox="0 0 1126 890">
    <polygon points="0,95 1126,0 1126,800 0,875" fill="#0b3a6e"/>
    <polygon points="0,0 0,95 186,95" fill="#00AB8E"/>
    <polygon points="935,800 1126,742 1126,880" fill="#00AB8E"/>
  </svg>
  <div class="abs dot-grid" style="left:985px;top:1472px;grid-template-columns:repeat(5,4px)">
    <i></i><i></i><i></i><i></i><i></i><i></i><i></i><i></i><i></i><i></i><i></i><i></i><i></i><i></i><i></i><i></i><i></i><i></i><i></i><i></i><i></i><i></i><i></i><i></i><i></i>
  </div>
  <div class="abs dot-grid" style="left:25px;top:2040px;grid-template-columns:repeat(5,4px)">
    <i></i><i></i><i></i><i></i><i></i><i></i><i></i><i></i><i></i><i></i><i></i><i></i><i></i><i></i><i></i><i></i><i></i><i></i><i></i><i></i><i></i><i></i><i></i><i></i><i></i>
  </div>
  <h2 class="abs center-title on-dark" style="top:1508px">Ares Of Expertise</h2>

  <div class="abs exp-card" style="left:188px;top:1596px">
    <div class="exp-photo" role="img" aria-label="Two colleagues working together on a laptop" style="background:linear-gradient(180deg,#d9dde2,#8d96a2)"></div>
    <div class="exp-red"></div>
    <div class="exp-icon"><svg width="26" height="26" viewBox="0 0 26 26" fill="none" stroke="#0b3a6e" stroke-width="1.5"><circle cx="13" cy="13" r="3"/><circle cx="13" cy="4" r="2"/><circle cx="4" cy="19" r="2"/><circle cx="22" cy="19" r="2"/><path d="M13 6v4M6 18l5-3M20 18l-5-3"/></svg></div>
    <div class="exp-label">NetWork Support</div>
  </div>
  <div class="abs exp-card" style="left:443px;top:1596px">
    <div class="exp-photo" role="img" aria-label="Hands holding a phone under a glowing digital globe" style="background:linear-gradient(180deg,#2b4a6a,#0d1c2e)"></div>
    <div class="exp-red"></div>
    <div class="exp-icon"><svg width="26" height="26" viewBox="0 0 26 26" fill="none" stroke="#0b3a6e" stroke-width="1.5"><path d="M4 11h4l10-6v16l-10-6H4z"/><path d="M8 15l2 7h3l-2-7"/><path d="M21 10l3-1M21 16l3 1"/></svg></div>
    <div class="exp-label">Marketing</div>
  </div>
  <div class="abs exp-card" style="left:698px;top:1596px">
    <div class="exp-photo" role="img" aria-label="Seedling growing from a stack of coins" style="background:linear-gradient(180deg,#5a4a3c,#1f1a16)"></div>
    <div class="exp-red"></div>
    <div class="exp-icon"><svg width="26" height="26" viewBox="0 0 26 26" fill="none" stroke="#0b3a6e" stroke-width="1.5"><path d="M4 22h18"/><rect x="5" y="14" width="4" height="8"/><rect x="11" y="10" width="4" height="12"/><rect x="17" y="6" width="4" height="16"/><path d="M5 9l6-4 4 3 7-5"/></svg></div>
    <div class="exp-label">Raising Capital</div>
  </div>
  <div class="abs exp-card" style="left:188px;top:1877px">
    <div class="exp-photo" role="img" aria-label="Business handshake over a desk" style="background:linear-gradient(180deg,#c7c2bc,#7b756e)"></div>
    <div class="exp-red"></div>
    <div class="exp-icon"><svg width="26" height="26" viewBox="0 0 26 26" fill="none" stroke="#0b3a6e" stroke-width="1.5"><path d="M2 12l5-4 5 3 5-3 7 4"/><path d="M7 14l4 4 2-1 2 2 2-1 3-3"/><path d="M12 11l-3 3"/></svg></div>
    <div class="exp-label">Mergers &amp; Acquistion</div>
  </div>
  <div class="abs exp-card" style="left:443px;top:1877px">
    <div class="exp-photo" role="img" aria-label="Hand writing figures next to a calculator" style="background:linear-gradient(180deg,#d9d7d2,#9c9892)"></div>
    <div class="exp-red"></div>
    <div class="exp-icon"><svg width="26" height="26" viewBox="0 0 26 26" fill="none" stroke="#0b3a6e" stroke-width="1.5"><path d="M4 22h18"/><rect x="6" y="15" width="3" height="7"/><rect x="11" y="11" width="3" height="11"/><rect x="16" y="7" width="3" height="15"/><path d="M5 11l5-5 4 3 6-6"/></svg></div>
    <div class="exp-label">Revenue Acceleration</div>
  </div>
  <div class="abs exp-card" style="left:698px;top:1877px">
    <div class="exp-photo" role="img" aria-label="Businessman beside a large integration diagram on a screen" style="background:linear-gradient(180deg,#e4e9ef,#9fb1c4)"></div>
    <div class="exp-red"></div>
    <div class="exp-icon"><svg width="26" height="26" viewBox="0 0 26 26" fill="none" stroke="#0b3a6e" stroke-width="1.5"><circle cx="13" cy="13" r="4"/><circle cx="13" cy="13" r="9" stroke-dasharray="4 3"/></svg></div>
    <div class="exp-label">Integration &amp; Incubation</div>
  </div>

  <!-- testimonials -->
  <h2 class="abs center-title on-light" style="top:2280px">OUR TESTIMONIALS</h2>
  <div class="abs t-card" style="left:188px">
    <div class="t-quote">&ldquo;</div>
    <div class="t-avatar" role="img" aria-label="Portrait of the client"></div>
    <div class="t-name">Owen Castell</div>
    <p class="t-text">Lorem ipsum dolor sit amet, consectetur adipiscing elit, sed do eiusmod tempor incididunt</p>
    <div class="t-stars"><svg width="112" height="18" viewBox="0 0 112 18"><g fill="#111"><path id="st" d="M9 1l2.4 5.4 5.8.5-4.4 3.8 1.3 5.7L9 13.4 3.9 16.4l1.3-5.7L.8 6.9l5.8-.5z"/><use href="#st" x="23"/><use href="#st" x="46"/><use href="#st" x="69"/><use href="#st" x="92"/></g></svg></div>
  </div>
  <div class="abs t-card" style="left:443px">
    <div class="t-quote">&ldquo;</div>
    <div class="t-avatar" role="img" aria-label="Portrait of the client"></div>
    <div class="t-name">Maya Linwood</div>
    <p class="t-text">Lorem ipsum dolor sit amet, consectetur adipiscing elit, sed do eiusmod tempor incididunt</p>
    <div class="t-stars"><svg width="112" height="18" viewBox="0 0 112 18"><g fill="#111"><use href="#st"/><use href="#st" x="23"/><use href="#st" x="46"/><use href="#st" x="69"/><use href="#st" x="92"/></g></svg></div>
  </div>
  <div class="abs t-card" style="left:697px">
    <div class="t-quote">&ldquo;</div>
    <div class="t-avatar" role="img" aria-label="Portrait of the client"></div>
    <div class="t-name">Idris Fenton</div>
    <p class="t-text">Lorem ipsum dolor sit amet, consectetur adipiscing elit, sed do eiusmod tempor incididunt</p>
    <div class="t-stars"><svg width="112" height="18" viewBox="0 0 112 18"><g fill="#111"><use href="#st"/><use href="#st" x="23"/><use href="#st" x="46"/><use href="#st" x="69"/><use href="#st" x="92"/></g></svg></div>
  </div>
  <div class="abs pager" style="top:2735px"><i></i><i></i><i class="on"></i><i></i><i></i></div>

  <!-- approach -->
  <h2 class="abs section-title" style="left:186px;top:2835px">OUR APPROACH</h2>
  <div class="abs body-text" style="left:188px;top:2887px;width:290px">
    <p>We've built our approach to helping your startup thrive based around three key developmental pillars that guarantee results for our partners.</p>
    <p>First pillar is expertise. We've built our firm on a bank of insights, knowledge and proficiencies honed over years of working with the biggest names in venture capitalism – that experience forms the backbone of every project, every pitch and every investment.</p>
    <p>Second pillar is collaboration. We believe that the best partnerships start with a combined and cooperative approach that benefits all parties every step of the way. We'll always keep our partners up-to-date with our work using regular touchpoints and reports.</p>
  </div>
  <a class="abs btn" style="left:188px;top:3219px;width:99px;height:27px">Read More</a>
  <div class="abs approach-photo" role="img" aria-label="Hand placing a dart into the centre of a dartboard"></div>

  <!-- blog -->
  <svg class="abs" style="left:0;top:3312px" width="1126" height="770" viewBox="0 0 1126 770">
    <polygon points="0,85 1126,0 1126,675 0,757" fill="#0b3a6e"/>
    <polygon points="0,0 0,85 186,85" fill="#00AB8E"/>
    <polygon points="935,676 1126,668 1126,770" fill="#00AB8E"/>
  </svg>
  <h2 class="abs center-title on-dark" style="top:3432px">OUR LATEST BLOG &amp; POST</h2>

  <article class="abs b-card" style="left:188px">
    <div class="b-photo" role="img" aria-label="Hand drawing a rising blue bar chart" style="background:linear-gradient(160deg,#f2f3f5,#b8c4d2)"></div>
    <div class="b-date">25<br>FEB</div>
    <h3 class="b-title">Lorem Ipsum is simply dummy</h3>
    <p class="b-text">Lorem ipsum dolor sit amet, consectetur adipiscing elit, sed do eiusmod tempor</p>
    <a class="b-more">Read More</a>
  </article>
  <article class="abs b-card" style="left:443px">
    <div class="b-photo" role="img" aria-label="Printed financial charts and graphs on a desk" style="background:linear-gradient(160deg,#e6edf3,#8fa7bf)"></div>
    <div class="b-date">25<br>FEB</div>
    <h3 class="b-title">Lorem Ipsum is simply dummy</h3>
    <p class="b-text">Lorem ipsum dolor sit amet, consectetur adipiscing elit, sed do eiusmod tempor</p>
    <a class="b-more">Read More</a>
  </article>
  <article class="abs b-card" style="left:696px">
    <div class="b-photo" role="img" aria-label="Dark board with the word marketing and a colourful chart" style="background:linear-gradient(160deg,#3b4048,#15181d)"></div>
    <div class="b-date">25<br>FEB</div>
    <h3 class="b-title">Lorem Ipsum is simply dummy</h3>
    <p class="b-text">Lorem ipsum dolor sit amet, consectetur adipiscing elit, sed do eiusmod tempor</p>
    <a class="b-more">Read More</a>
  </article>
  <div class="abs pager dark" style="top:3937px"><i></i><i></i><i class="on"></i><i></i><i></i></div>

  <!-- contact -->
  <h2 class="abs center-title on-light" style="top:4090px">Get In Touch</h2>
  <div class="abs field" style="left:295px;top:4181px;width:262px;height:36px">Name</div>
  <div class="abs field" style="left:570px;top:4181px;width:261px;height:36px">Phone Number</div>
  <div class="abs field" style="left:295px;top:4230px;width:536px;height:36px">Email Id</div>
  <div class="abs field" style="left:295px;top:4279px;width:536px;height:101px">Messages</div>
  <a class="abs submit">Submit</a>

  <!-- footer -->
  <footer class="abs footer">
    <div class="abs brand">HOLVENCREST VENTURES</div>
    <p class="abs foot-about">Lorem ipsum dolor sit amet, consectetur adipiscing elit, sed do eiusmod tempor incididunt ut labore et dolore magna aliqua. Quis ipsum suspendisse</p>

    <div class="abs foot-head" style="left:477px;top:74px">Contact Us</div>
    <ul class="abs foot-list" style="left:477px;top:96px;width:170px;line-height:13px">
      <li style="align-items:flex-start;margin-bottom:12px"><svg width="10" height="13" viewBox="0 0 10 13" style="flex:none;margin-top:1px"><path d="M5 0a5 5 0 015 5c0 3.5-5 8-5 8S0 8.5 0 5a5 5 0 015-5z" fill="#fff"/><circle cx="5" cy="5" r="2" fill="#082b52"/></svg><span>418 Elm Row, Harlow, OK,<br>74100</span></li>
      <li style="margin-bottom:12px"><svg width="10" height="10" viewBox="0 0 10 10" style="flex:none"><path d="M2 0l2 3-1 1.5c.8 1.5 1.7 2.4 3 3L7.5 6l2.5 2-1 2C4 10 0 6 0 1z" fill="#fff"/></svg><span>(000) 555-0142</span></li>
      <li><svg width="11" height="8" viewBox="0 0 11 8" style="flex:none"><rect width="11" height="8" fill="#fff"/><path d="M0 0l5.5 4.5L11 0" stroke="#082b52" fill="none"/></svg><span>info@holvencrest.com</span></li>
    </ul>

    <div class="abs foot-head" style="left:672px;top:74px">Information</div>
    <ul class="abs foot-list" style="left:672px;top:94px">
      <li>Home</li><li>Service</li><li>Blog</li><li>Contact</li>
    </ul>

    <div class="abs foot-head" style="left:829px;top:74px">Follow Us</div>
    <ul class="abs foot-list" style="left:829px;top:94px">
      <li><span class="mk"></span>Facefeed</li>
      <li><span class="mk"></span>Picstream</li>
      <li><span class="mk"></span>Chirper</li>
      <li><span class="mk"></span>Searchly</li>
    </ul>

    <div class="abs foot-rule"></div>
    <div class="abs foot-copy">© 2021 holvencrest All Rights Reserved.</div>
  </footer>
</main>
</body>
</html>
```